NEW Modern Sleek Business Card for VR Language Startup

Our startup is using VR to lead the next wave of world language education. We need a two-sided business card that introduces the larger organization (Quorvel Language Inc) and our contact info on one side and shows the product, Lumidrasca, on the other side.

Side 1 (contact info)= Quorvel Logo and Contact info (name, title, phone, email)

Side 2 (product)= Lumidrasc logo, text, and website
Text= Culturally Immersive Language Learning Games
Website= www.lumidrasc.example

Target Market(s)

Education, Technology

Contact Information for Business Card

Contact info will be updated upon approval of the design. For now, put this as a placeholder.

Perry Hollins
Founder & CEO
phollins@mailtrove.example
(555)-014-2736

Font styles to use
Other font styles liked:
• Gibson and Century Gothic are the brand fonts

Requirements
Nice to have
• I would love to see cohesion between the design and colors of the two logos. I have attached a few business card designs that I like, so you can get a feel for my preferred style.

```html
<!DOCTYPE html>
<html lang="en">
<head>
<meta charset="utf-8">
<title>Quorvel Language – Business Card</title>
<link rel="stylesheet" href="https://fonts.googleapis.com/css2?family=Questrial&family=Montserrat:wght@700&display=swap">
<style>
  :root {
    --canvas-bg: #e6e6e8;
    --card-black: #121213;
    --card-pattern: #1d1d1f;
    --text-white: #f4f4f4;
    --text-grey: #8c8c90;
    --accent-orange: #f7a23b;
    --accent-pink: #ec3f7e;
    --accent-purple: #a65de0;
    --accent-blue: #4fc3f2;
    --mark-dot: #ec4a7c;
  }
  * { box-sizing: border-box; margin: 0; padding: 0; }
  html, body {
    width: 1200px; height: 900px; overflow: hidden;
    background: var(--canvas-bg);
    font-family: "Questrial", "Century Gothic", sans-serif;
  }
  .card-sheet {
    width: 1200px; height: 900px;
    display: flex; flex-direction: column; align-items: center; justify-content: center;
    gap: 56px;
  }
  .business-card {
    position: relative;
    width: 630px; height: 360px;
    border-radius: 6px;
    overflow: hidden;
    box-shadow: 0 10px 30px rgba(0,0,0,0.18);
  }
  /* Side 1 – contact */
  .card-contact { background: var(--card-black); }
  .contact-block { position: absolute; left: 42px; top: 38px; color: var(--text-white); }
  .contact-name {
    font-family: "Montserrat", "Century Gothic", sans-serif;
    font-weight: 700; font-size: 22px; letter-spacing: 0.3px;
  }
  .contact-title { font-size: 12px; color: var(--text-grey); margin-top: 3px; }
  .contact-line {
    display: flex; align-items: center; gap: 9px;
    font-size: 13px; margin-top: 9px;
  }
  .contact-line:first-of-type { margin-top: 14px; }
  .contact-icon { width: 15px; height: 15px; flex: none; }
  .brand-lockup {
    position: absolute; display: flex; align-items: center; gap: 16px;
  }
  .card-contact .brand-lockup { right: 60px; top: 172px; }
  .brand-dot {
    width: 58px; height: 58px; border-radius: 50%;
    background: var(--mark-dot); flex: none;
  }
  .brand-name {
    font-size: 38px; letter-spacing: 7px; text-transform: uppercase;
    color: var(--text-white); font-weight: 400;
  }
  /* Side 2 – product */
  .card-product { background: var(--card-black); }
  .product-pattern-area {
    position: absolute; inset: 0;
    background: radial-gradient(circle at 60% 55%, var(--card-pattern), var(--card-black) 80%);
  }
  .card-product .brand-lockup { left: 60px; top: 46px; }
  .card-product .brand-dot { width: 50px; height: 50px; }
  .card-product .brand-name { font-size: 32px; letter-spacing: 6px; }
  .product-tagline {
    position: absolute; left: 60px; top: 142px;
    font-size: 21px; letter-spacing: 0.4px;
    background: linear-gradient(90deg, var(--accent-orange), var(--accent-pink) 35%, var(--accent-purple) 68%, var(--accent-blue));
    -webkit-background-clip: text; background-clip: text; color: transparent;
  }
  .product-website {
    position: absolute; left: 60px; bottom: 52px;
    font-size: 13px; color: var(--text-grey); letter-spacing: 0.5px;
  }
</style>
</head>
<body>
<main class="card-sheet">

  <section class="business-card card-contact" aria-label="Business card, contact side">
    <div class="contact-block">
      <h1 class="contact-name">Perry Hollins</h1>
      <p class="contact-title">Founder &amp; CEO</p>
      <p class="contact-line">
        <svg class="contact-icon" viewBox="0 0 24 24" aria-hidden="true">
          <path d="M6.6 10.8a15 15 0 0 0 6.6 6.6l2.2-2.2a1 1 0 0 1 1-.25 11.4 11.4 0 0 0 3.6.57 1 1 0 0 1 1 1V20a1 1 0 0 1-1 1A17 17 0 0 1 3 4a1 1 0 0 1 1-1h3.5a1 1 0 0 1 1 1c0 1.25.2 2.45.57 3.6a1 1 0 0 1-.25 1z" fill="none" stroke="#ec3f7e" stroke-width="1.8"/>
        </svg>
        (555)-014-2736
      </p>
      <p class="contact-line">
        <svg class="contact-icon" viewBox="0 0 24 24" aria-hidden="true">
          <rect x="2" y="5" width="20" height="14" rx="1.5" fill="#4fc3f2"/>
          <path d="M2 6l10 7 10-7" fill="none" stroke="#121213" stroke-width="1.8"/>
        </svg>
        phollins@mailtrove.example
      </p>
    </div>
    <div class="brand-lockup">
      <span class="brand-dot" aria-hidden="true"></span>
      <span class="brand-name">Quorvel</span>
    </div>
  </section>

  <section class="business-card card-product" aria-label="Business card, product side">
    <div class="product-pattern-area" role="img" aria-label="Faint repeating pattern of the product mark in dark grey"></div>
    <div class="brand-lockup">
      <span class="brand-dot" aria-hidden="true"></span>
      <span class="brand-name">Lumidrasc</span>
    </div>
    <p class="product-tagline">Culturally Immersive Language Learning Games</p>
    <p class="product-website">www.lumidrasc.example</p>
  </section>

</main>
</body>
</html>
```